HomePage Design for Lumen Getaways - once-in-a-lifetime experiences for busy working people

Design a homepage for the Lumen Getaways (www.lumengetaways.example) website compatible with further web pages and the design briefing documents attached

LG HomePage Design Brief
We are seeking website HomePage designs incorporating our new Logo and colour scheme, for Lumen Getaways (www.lumengetaways.example) to go with the site functionality and wireframe ideas attached.
The website HomePage design needs to
• Incorporate and be consistent with the LG Logo and its colour scheme attached.
• Express the brand values of being inspirational, high quality, upscale, cultured, aspirational, and contemporary – even somewhat ‘hip’. Probably positioned somewhere between Harlow Pike (Deluxe Travel) and Green Walrus (Hip Travel) – see https://www.harlowpike.example and https://www.greenwalrus.example .
• Be instantly recognisable and different from other travel websites and instantly communicate the nature of the brand proposition and target customer base.
• Appeal to our core 25-55 affluent businesspeople demographic
• Work in the UK, US/Canada and Australia/NZ and ultimately in mainland Europe.
• Use fonts and colours that are easily reproduced online and compatible with nearly all browsers.
• Be part of a responsive website design, that can be used both on Desktops and laptops but also with tablets and mobile ‘phones (hence content not too wide across the page)
• Feature the strapline ‘Lumen Getaways in less than 7 Days’
• Work with the and wireframes and processes shown in the attached presentation – although intended as a guide only these features and processes all need to be incorporated into the HomePage.
• Make full use of high quality images and video to convey our brand proposition and products

Target Market(s)

25-55 affluent businesspeople

Industry/Entity Type

Travel Industry

Number of Pages Required

1 page

Font styles to use
Sans Serif

Colors
0455a3
00a88f

Requirements
Must have
• • Incorporate and be consistent with the LG Logo and its colour scheme attached.
• • Express the brand values of being inspirational, high quality, upscale, cultured, aspirational, and contemporary – even somewhat ‘hip’. Probably positioned somewhere between Harlow Pike (Deluxe Travel) and Green Walrus (Hip Travel) – see https://www.harlowpike.example and https://www.greenwalrus.example .
• • Be instantly recognisable and different from other travel websites and instantly communicate the nature of the brand proposition and target customer base.
• • Appeal to our core 25-55 affluent businesspeople demographic
• • Be part of a responsive website design, that can be used both on Desktops and laptops but also with tablets and mobile ‘phones (hence content not too wide across the page)
• • Feature the strapline ‘Lumen Getaways in less than 7 Days’
• • Work with the and wireframes and processes shown in the attached presentation – although intended as a guide only these features and processes all need to be incorporated into the HomePage.
• • Make full use of high quality images and video to convey our brand proposition and products
• Colours as per Logo not as shown below
Nice to have
• • Work in the UK, US/Canada and Australia/NZ and ultimately in mainland Europe.
Should not have
• Must not be cheap or mass-market, nor excessively "stuffy or luxury-orientated"

```html
<!DOCTYPE html>
<html lang="en">
<head>
<meta charset="utf-8">
<title>Lumen Getaways — Home</title>
<link rel="stylesheet" href="https://fonts.googleapis.com/css2?family=Open+Sans:wght@300;400;600;700&family=Roboto:wght@400;500;700&display=swap">
<style>
:root{
  --green:#1e5b2c;
  --navy:#263878;
  --accent-blue:#1f3a93;
  --orange:#f7a11a;
  --page:#f4f4f4;
  --ink:#444;
  --footer:#1b1b1b;
  --white:#fff;
}
*{margin:0;padding:0;box-sizing:border-box}
html,body{width:802px;height:1200px;overflow:hidden}
body{position:relative;background:var(--white);font-family:"Open Sans",sans-serif;color:var(--ink)}
.abs{position:absolute}

.topbar{left:0;top:0;width:802px;height:28px;background:var(--green)}
.topbar-links{left:86px;top:9px;font:400 8.4px "Roboto",sans-serif;color:var(--white);white-space:nowrap}
.topbar-links span{margin:0 3px}
.social-dot{width:14px;height:14px;border-radius:50%;background:var(--white);top:7px;display:flex;align-items:center;justify-content:center}
.social-dot svg{display:block}

.header{left:0;top:28px;width:802px;height:50px;background:var(--white);border-bottom:2px solid var(--accent-blue)}
.brand{left:86px;top:46px;display:flex;align-items:center;gap:6px;font:700 10.5px "Open Sans",sans-serif;color:var(--green);white-space:nowrap}
.brand-mark{width:13px;height:13px;border-radius:50%;background:var(--green)}
.nav{top:50px;font:400 9px "Open Sans",sans-serif;color:#555;white-space:nowrap}
.nav-pointer{left:411px;top:71px;width:0;height:0;border-left:5px solid transparent;border-right:5px solid transparent;border-bottom:5px solid var(--accent-blue)}

.hero{left:0;top:78px;width:802px;height:308px;background:linear-gradient(180deg,#0d2f7a 0%,#1b4fa6 35%,#c77a1e 70%,#6b4a22 100%)}

.experiences{left:0;top:386px;width:802px;height:570px;background:var(--page)}
.strapline{left:0;top:400px;width:802px;text-align:center;font:300 21.6px "Open Sans",sans-serif;color:#444;white-space:nowrap}
.tile{display:flex;align-items:center;justify-content:center;font:700 13.5px "Roboto",sans-serif;color:var(--white);white-space:nowrap}
.tile-wildlife{left:86px;top:445px;width:368px;height:216px;background:linear-gradient(160deg,#1f3c7a,#3a5f8f 50%,#c9d3e0)}
.tile-festivals{left:462px;top:445px;width:253px;height:216px;background:linear-gradient(180deg,#c93a2a,#d96b34 40%,#6b1f1f)}
.tile-activities{left:86px;top:672px;width:253px;height:216px;background:linear-gradient(180deg,#6c7a84,#4d5a46 55%,#3a3530)}
.tile-events{left:347px;top:672px;width:368px;height:216px;background:linear-gradient(180deg,#4a5670,#5f6b78 45%,#707880)}

.btn-view{left:353px;top:908px;width:96px;height:26px;background:var(--navy);color:var(--white);font:600 8.5px "Roboto",sans-serif;display:flex;align-items:center;justify-content:center}

.newsletter{left:0;top:966px;width:802px;height:58px;background:var(--green)}
.newsletter-title{left:163px;top:988px;font:500 11.5px "Roboto",sans-serif;color:var(--white);white-space:nowrap}
.newsletter-input{left:297px;top:984px;width:205px;height:20px;background:var(--white);border-radius:2px;font:400 7.5px "Open Sans",sans-serif;color:#999;padding:6px 6px}
.newsletter-btn{left:509px;top:984px;width:63px;height:20px;background:var(--orange);color:var(--white);font:700 8.5px "Roboto",sans-serif;display:flex;align-items:center;justify-content:center;border-radius:1px}

.footer{left:0;top:1024px;width:802px;height:176px;background:var(--footer)}
.footer-col{top:1043px;font:400 8.6px/13.7px "Open Sans",sans-serif;color:#e6e6e6;white-space:nowrap}
.footer-social{top:1122px;width:12px;height:12px}
.footer-rule{left:216px;top:1152px;width:368px;height:1px;background:#4a4a4a}
.copyright{left:0;top:1172px;width:802px;text-align:center;font:400 8px "Open Sans",sans-serif;color:#e6e6e6}
</style>
</head>
<body>

<div class="abs topbar"></div>
<div class="abs topbar-links">Pioneers Club<span>|</span>Client Log-In<span>|</span>Vlogs &amp; Reviews</div>

<div class="abs social-dot" style="left:650px" aria-label="Email">
  <svg width="8" height="6" viewBox="0 0 8 6"><rect x="0.5" y="0.5" width="7" height="5" fill="none" stroke="#1e5b2c"/><polyline points="0.5,0.5 4,3.3 7.5,0.5" fill="none" stroke="#1e5b2c"/></svg>
</div>
<div class="abs social-dot" style="left:668px" aria-label="Share">
  <svg width="8" height="8" viewBox="0 0 8 8"><circle cx="6.2" cy="1.6" r="1.3" fill="#1e5b2c"/><circle cx="1.8" cy="4" r="1.3" fill="#1e5b2c"/><circle cx="6.2" cy="6.4" r="1.3" fill="#1e5b2c"/><polyline points="6.2,1.6 1.8,4 6.2,6.4" fill="none" stroke="#1e5b2c" stroke-width="0.8"/></svg>
</div>
<div class="abs social-dot" style="left:685px" aria-label="Website">
  <svg width="8" height="8" viewBox="0 0 8 8"><circle cx="4" cy="4" r="3.4" fill="none" stroke="#1e5b2c" stroke-width="0.9"/><ellipse cx="4" cy="4" rx="1.4" ry="3.4" fill="none" stroke="#1e5b2c" stroke-width="0.8"/><line x1="0.6" y1="4" x2="7.4" y2="4" stroke="#1e5b2c" stroke-width="0.8"/></svg>
</div>
<div class="abs social-dot" style="left:703px" aria-label="Chat">
  <svg width="8" height="8" viewBox="0 0 8 8"><path d="M1 1.2h6v4H3.4L1.6 6.8V5.2H1z" fill="#1e5b2c"/></svg>
</div>

<div class="abs header"></div>
<div class="abs brand"><span class="brand-mark"></span>Lumen Getaways</div>
<div class="abs nav" style="left:392px">Destinations</div>
<div class="abs nav" style="left:455px">Experiences</div>
<div class="abs nav" style="left:515px">Trips by Month</div>
<div class="abs nav" style="left:591px">Topical Now</div>
<div class="abs nav" style="left:657px">Tailored</div>
<svg class="abs" style="left:702px;top:49px" width="13" height="13" viewBox="0 0 13 13" aria-label="Search">
  <circle cx="5.5" cy="5.5" r="4.2" fill="none" stroke="#666" stroke-width="1.4"/>
  <line x1="8.6" y1="8.6" x2="12" y2="12" stroke="#666" stroke-width="1.6"/>
</svg>
<div class="abs nav-pointer"></div>

<div class="abs hero" role="img" aria-label="Ancient amphitheatre lit up at dusk beneath a deep blue sky"></div>

<div class="abs experiences"></div>
<h1 class="abs strapline">Lumen Getaways in less than 7 Days!</h1>

<div class="abs tile tile-wildlife" role="img" aria-label="Arctic wildlife on snow under the northern lights">Wonders of Wildlife</div>
<div class="abs tile tile-festivals" role="img" aria-label="Crowd with flags at a colourful music festival">World’s Greatest Festivals</div>
<div class="abs tile tile-activities" role="img" aria-label="Mountain town street with flower baskets">Must Do Activities</div>
<div class="abs tile tile-events" role="img" aria-label="Viewing platform overlooking a mountain valley">Unique Annual Events</div>

<div class="abs btn-view">VIEW ALL</div>

<div class="abs newsletter"></div>
<div class="abs newsletter-title">GET OUR NEWSLETTER</div>
<div class="abs newsletter-input">Your email here..</div>
<div class="abs newsletter-btn">SIGN IN</div>

<div class="abs footer" role="img" aria-label="Dark street map backdrop"></div>
<div class="abs footer-col" style="left:102px">About Us<br>Our Partners<br>Newsletter<br>FAQs</div>
<div class="abs footer-col" style="left:194px">Contacts Us<br>Booking Conditions<br>Privacy &amp; Cookies<br>Terms of Use</div>
<div class="abs footer-col" style="left:310px">Financial Protection<br>Travel Insurance<br>Visas<br>Travel Advice</div>
<div class="abs footer-col" style="left:428px">Group Bookings<br>Tailor-Made &amp; Extra Nights<br>Booking Flights<br>Careers with LG</div>
<div class="abs footer-col" style="left:567px">LG Protecting wildlife &amp; animals,<br>and supporting local communities<br>Press Room</div>

<svg class="abs footer-social" style="left:356px" viewBox="0 0 12 12" aria-label="Email"><rect x="1" y="2.5" width="10" height="7" fill="none" stroke="#fff" stroke-width="1.2"/><polyline points="1,2.5 6,6.5 11,2.5" fill="none" stroke="#fff" stroke-width="1.2"/></svg>
<svg class="abs footer-social" style="left:381px" viewBox="0 0 12 12" aria-label="Share"><circle cx="9.5" cy="2.5" r="1.8" fill="#fff"/><circle cx="2.5" cy="6" r="1.8" fill="#fff"/><circle cx="9.5" cy="9.5" r="1.8" fill="#fff"/><polyline points="9.5,2.5 2.5,6 9.5,9.5" fill="none" stroke="#fff" stroke-width="1.1"/></svg>
<svg class="abs footer-social" style="left:408px" viewBox="0 0 12 12" aria-label="Website"><circle cx="6" cy="6" r="5" fill="none" stroke="#fff" stroke-width="1.2"/><ellipse cx="6" cy="6" rx="2.1" ry="5" fill="none" stroke="#fff" stroke-width="1"/><line x1="1" y1="6" x2="11" y2="6" stroke="#fff" stroke-width="1"/></svg>
<svg class="abs footer-social" style="left:435px" viewBox="0 0 12 12" aria-label="Chat"><path d="M1 1.5h10v6.5H5L2.2 10.6V8H1z" fill="#fff"/></svg>

<div class="abs footer-rule"></div>
<div class="abs copyright">© 2017 &nbsp;Lumen Getaways All Rights Reserved.</div>

</body>
</html>
```